Webshop facelift - modern, sales oriented, mobile first

We need facelifted webshop, which is running for few years.
www.lunavix.si
Some of the basic requirements:

1.) Logo must basicly stay the same, it could only be a little "modernised".
2.) Main goal is to generate more sales, so webpage must be much more sales oriented.
3.) Focus is on category page and product page. Those two page types must be realy designed very well
4.) Mobile first, there are 80% customers over mobile devices
5.) Mobile menu must be also much better
6.) Category description will go under listed products
7.) On product page, there must be much bigger product images, and also mobile friendly image slider
8.) Big add to cart buttons
9.) Badges about safe shopping, possible returning goods, 100% warranty
10.) exposed product videos, images between text
11.) cleary exposed product benefits
11.) Products, which have sizes to choose, must have more user friendly choose option
12.) category page on desktop can have only products in all width, not side menu on the left
13.) Exposed CTA's on product page

You can create this category page: https://lunavix.si/posteljnina
You can create this product page: https://lunavix.si/shujsevalni-steznik-turmalin-shorts

In short: mobile first, very sales oriented, look like 2018, big images, great shopping experience.

Target Market(s)

6 European coutries

Industry/Entity Type

E-Commerce

Number of Pages Required

3 page

Font styles to use
Sans Serif

Colors

Designer to choose colors to be used in the design.

Requirements
Must have
• Mobile first design
• Big images
• Very sales oriented
• CTA's through product description
Nice to have
• Product badges, like for example "100% cotton", "On stock", "Sale", "New"
Should not have
• Should not be copied from somewhere.

```html
<!DOCTYPE html>
<html lang="en">
<head>
<meta charset="utf-8">
<title>Lunavix – Mobile Home</title>
<link href="https://fonts.googleapis.com/css2?family=Montserrat:wght@400;500;600;700&display=swap" rel="stylesheet">
<style>
  :root {
    --orange: #f7901e;
    --navy: #1f3a5a;
    --ink: #2b2b2b;
    --muted: #8a8a8a;
    --line: #e2e2e2;
    --bar: #f4f4f4;
    --white: #ffffff;
    --hero-dark: #3a3a3a;
    --hero-light: #7b7b7b;
  }
  * { box-sizing: border-box; margin: 0; padding: 0; }
  html, body { width: 800px; height: 1200px; overflow: hidden; }
  body {
    font-family: "Montserrat", sans-serif;
    background: var(--white);
    color: var(--ink);
    position: relative;
  }
  .top-bar {
    height: 115px;
    background: var(--bar);
    display: flex;
    align-items: center;
    justify-content: space-between;
    padding: 0 40px;
  }
  .contact-icons { display: flex; gap: 22px; align-items: center; }
  .contact-icon {
    width: 56px; height: 56px;
    border: 3px solid var(--orange);
    border-radius: 50%;
    display: flex; align-items: center; justify-content: center;
  }
  .contact-icon.small { width: 46px; height: 46px; }
  .currency-toggle {
    display: flex; align-items: center; gap: 12px;
    background: var(--navy);
    color: var(--white);
    font-weight: 600; font-size: 22px;
    border-radius: 30px;
    padding: 8px 8px 8px 22px;
  }
  .currency-toggle .knob {
    width: 36px; height: 36px; border-radius: 50%;
    background: var(--white);
  }
  .site-header {
    height: 140px;
    display: flex; align-items: center; justify-content: space-between;
    padding: 0 40px;
  }
  .brand { display: flex; align-items: center; gap: 18px; }
  .brand-mark { width: 64px; height: 64px; border-radius: 50%; background: var(--orange); }
  .brand-name { font-size: 50px; font-weight: 700; color: var(--navy); }
  .menu-toggle { display: flex; flex-direction: column; gap: 9px; }
  .menu-toggle span { display: block; width: 46px; height: 5px; background: var(--navy); border-radius: 3px; }
  .search {
    margin: 0 40px;
    height: 62px;
    border-bottom: 2px solid var(--line);
    display: flex; align-items: center; justify-content: space-between;
    padding: 0 14px;
    font-size: 24px; color: var(--muted);
  }
  .hero {
    margin-top: 14px;
    height: 456px;
    position: relative;
    display: flex; flex-direction: column; align-items: center; justify-content: center;
    text-align: center;
  }
  .hero-photo {
    position: absolute; inset: 0;
    background: linear-gradient(110deg, var(--hero-dark) 0%, var(--hero-light) 45%, var(--hero-dark) 100%);
  }
  .hero-title {
    position: relative;
    color: var(--white);
    font-size: 46px; font-weight: 700; line-height: 1.3;
  }
  .cta {
    position: relative;
    margin-top: 44px;
    background: var(--orange);
    color: var(--white);
    font-weight: 700; font-size: 22px; letter-spacing: 1px;
    padding: 20px 52px;
    border-radius: 40px;
  }
  .categories { padding-top: 56px; }
  .section-title {
    text-align: center;
    font-size: 40px; font-weight: 700;
    margin-bottom: 48px;
  }
  .category-photo {
    margin: 0 40px;
    height: 260px;
    background: linear-gradient(135deg, #e9e7e2 0%, #cfcac1 50%, #8f8b84 100%);
  }
</style>
</head>
<body>
  <div class="top-bar">
    <div class="contact-icons">
      <div class="contact-icon">
        <svg width="26" height="26" viewBox="0 0 24 24" fill="none" stroke="#f7901e" stroke-width="2.4" stroke-linecap="round" stroke-linejoin="round"><path d="M5 3h4l2 5-3 2a12 12 0 0 0 6 6l2-3 5 2v4a2 2 0 0 1-2 2A17 17 0 0 1 3 5a2 2 0 0 1 2-2z"/></svg>
      </div>
      <div class="contact-icon small">
        <svg width="22" height="22" viewBox="0 0 24 24" fill="none" stroke="#f7901e" stroke-width="2.4" stroke-linejoin="round"><rect x="3" y="6" width="18" height="12" rx="1"/><path d="M3 7l9 6 9-6"/></svg>
      </div>
      <div class="contact-icon small">
        <svg width="22" height="22" viewBox="0 0 24 24" fill="none" stroke="#f7901e" stroke-width="2.4" stroke-linecap="round"><circle cx="12" cy="12" r="8"/><path d="M12 8v4l3 2"/></svg>
      </div>
    </div>
    <div class="currency-toggle">EUR <span class="knob"></span></div>
  </div>

  <header class="site-header">
    <div class="brand">
      <span class="brand-mark"></span>
      <span class="brand-name">Lunavix</span>
    </div>
    <div class="menu-toggle" aria-label="Menu"><span></span><span></span><span></span></div>
  </header>

  <div class="search">
    <span>Search</span>
    <svg width="24" height="24" viewBox="0 0 24 24" fill="none" stroke="#2b2b2b" stroke-width="2.6" stroke-linecap="round"><circle cx="10" cy="10" r="6"/><path d="M15 15l5 5"/></svg>
  </div>

  <section class="hero">
    <div class="hero-photo" role="img" aria-label="Bedroom with jersey bed sheets in muted grey tones"></div>
    <h1 class="hero-title">Nuvo Sheets<br>Cloudsoft Cotton Jersey</h1>
    <span class="cta">ADD TO CART</span>
  </section>

  <section class="categories">
    <h2 class="section-title">Shop By Category</h2>
    <div class="category-photo" role="img" aria-label="Bedding category photo with white linens and cushions"></div>
  </section>
</body>
</html>
```